GLOBE Book Cover

1. Front & back cover designs (print-ready, high resolution PDF + PNG/JPEG).
2. Spine designs consistent across the series.
3. Mockup visuals (3D renders and group images).
4. Editable source files (AI/PSD/INDD).
5. Spine- 1.3572in x 10.3in, 2138px x 3075px.
6. Front- 7.1in x 10.3in with 0.125in bleed, 2138px x 3075px. Ideal resolution 300dpi.
7. Back- 7.1in x 10.3in with 0.125in bleed, 2138px x 3075px. Ideal resolution 300dpi.

```html
<!DOCTYPE html>
<html lang="en">
<head>
<meta charset="utf-8">
<title>GLOBE Book Cover</title>
<link href="https://fonts.googleapis.com/css2?family=Oswald:wght@400;500&display=swap" rel="stylesheet">
<style>
  :root {
    --backdrop: #283350;
    --paper: #dfe6ea;
    --ring-blue: #4a89dc;
    --navy: #243f7f;
    --ink: #253a7a;
    --photo-light: #b9b9b9;
    --photo-dark: #6f6f6f;
  }
  html, body {
    margin: 0;
    padding: 0;
    width: 1200px;
    height: 1001px;
    overflow: hidden;
    background: var(--backdrop);
  }
  .cover {
    position: absolute;
    left: 304px;
    top: 82px;
    width: 592px;
    height: 837px;
    background: var(--paper);
    overflow: hidden;
    font-family: "Oswald", sans-serif;
  }
  .cover-art {
    position: absolute;
    inset: 0;
    width: 100%;
    height: 100%;
  }
  .author {
    position: absolute;
    left: 0;
    width: 100%;
    top: 230px;
    margin: 0;
    text-align: center;
    font-size: 22px;
    font-weight: 500;
    color: var(--ink);
    letter-spacing: 0.2px;
    line-height: 1;
    padding-right: 8px;
    box-sizing: border-box;
  }
  .title {
    position: absolute;
    left: 0;
    width: 100%;
    top: 272px;
    margin: 0;
    text-align: center;
    font-size: 66px;
    font-weight: 500;
    line-height: 74px;
    color: var(--ink);
    text-transform: uppercase;
    letter-spacing: 0.5px;
    padding-right: 8px;
    box-sizing: border-box;
  }
  .imprint {
    position: absolute;
    left: 354px;
    top: 662px;
    margin: 0;
    font-size: 54px;
    font-weight: 400;
    line-height: 1;
    color: var(--ink);
    letter-spacing: 1px;
  }
</style>
</head>
<body>
  <div class="cover">
    <svg class="cover-art" viewBox="0 0 740 1046" preserveAspectRatio="none">
      <defs>
        <clipPath id="lower-zone">
          <rect x="0" y="813" width="740" height="233"/>
        </clipPath>
        <clipPath id="ring-zone">
          <rect x="0" y="0" width="740" height="701"/>
          <rect x="0" y="701" width="560" height="345"/>
        </clipPath>
        <linearGradient id="portrait-tone" x1="0" y1="0" x2="1" y2="1">
          <stop offset="0" stop-color="var(--photo-light)"/>
          <stop offset="1" stop-color="var(--photo-dark)"/>
        </linearGradient>
      </defs>

      <path class="base-band" clip-path="url(#lower-zone)" fill="var(--navy)" fill-rule="evenodd"
            d="M -420 280 A 790 790 0 1 0 1160 280 A 790 790 0 1 0 -420 280 Z
               M -105 515 A 475 475 0 1 0 845 515 A 475 475 0 1 0 -105 515 Z"/>

      <path class="quarter-band" fill="var(--navy)"
            d="M 20 485 A 358 358 0 0 0 378 843 L 378 891 A 406 406 0 0 1 -28 485 Z"/>

      <path class="open-ring" fill="none" stroke="var(--ring-blue)" stroke-width="40"
            clip-path="url(#ring-zone)"
            d="M 378 823 A 338 338 0 1 1 650 688"/>

      <rect class="portrait" x="612" y="0" width="128" height="234" fill="url(#portrait-tone)"
            role="img" aria-label="Greyscale portrait photo of the author, cropped at the top right corner"/>
    </svg>

    <p class="author">ADRIAN VELMONT PhD</p>
    <h1 class="title">Hidden Costs<br>In Innovation<br>Driven Growth<br>Companies</h1>
    <p class="imprint">GLOBE</p>
  </div>
</body>
</html>
```